Metal Recycling Website Require New Design for upgrade

Our company currently have an existing website, www.tavorinmetal.com and the website is generally outdated so we would like an improvement.

We would generally prefer to keep the current color theme of our website as it is similar to our current logo.

We would also like our company factory picture to be on somewhere of the webpage (but only if the designer think that the picture can blend well with the color theme)

Our company is dealing alot Aluminiun, Stainless Steel, Copper, Brass, Iron

Pictures uploaded.

Target Market(s)

General Commercial Manufacturer, B2B

Industry/Entity Type

Recycling

Number of Pages Required

1 page

Colors

Designer to choose colors to be used in the design.

Requirements
Must have
• Hopefully color will be similar to my logo theme but designer welcome to have their own input.
Nice to have
• Company Picture (Uploaded in the file)

```html
<!DOCTYPE html>
<html lang="en">
<head>
<meta charset="utf-8">
<title>Tavorin Metal Recycling</title>
<link href="https://fonts.googleapis.com/css2?family=Montserrat:wght@400;500;600;700;900&family=Raleway:ital,wght@0,400;0,500;0,600;0,700;1,400;1,500&family=Great+Vibes&display=swap" rel="stylesheet">
<style>
:root{
  --gold:#c9962a;
  --gold-light:#e2b84c;
  --gold-soft:#f0c24a;
  --dark:#2b2b2b;
  --ink:#2a2a2a;
  --text:#7a7a7a;
  --line:#e3e3e3;
  --grey-bg:#f5f5f5;
  --white:#fff;
}
*{margin:0;padding:0;box-sizing:border-box}
html,body{width:1200px;height:3517px;overflow:hidden}
body{font-family:'Raleway',sans-serif;color:var(--text);background:var(--white);position:relative}
.abs{position:absolute}
.btn{position:absolute;display:flex;align-items:center;justify-content:center;background:linear-gradient(90deg,var(--gold),var(--gold-light));color:#fff;font-family:'Montserrat',sans-serif;font-weight:700;font-size:10px;letter-spacing:.3px;text-transform:uppercase;border-radius:2px}
.center{text-align:center;left:0;width:1200px}
.eyebrow{font-size:10px;letter-spacing:1.5px;text-transform:uppercase;color:var(--gold-light)}
.heading{font-family:'Montserrat',sans-serif;font-weight:500;color:var(--ink);font-size:28px}
.rule{position:absolute;height:2px;width:38px;background:var(--gold)}

/* top bar */
.topbar{top:0;left:0;width:1200px;height:45px;background:var(--dark);color:#fff;font-size:11px;font-weight:500}
.topbar span{position:absolute;top:15px;display:flex;align-items:center;gap:7px}
/* header */
.header{top:45px;left:0;width:1200px;height:93px;background:#fff}
.brand{position:absolute;left:160px;top:29px;display:flex;align-items:center;gap:10px}
.brand i{width:36px;height:36px;border:3px solid var(--gold);display:block}
.brand b{font-family:'Montserrat',sans-serif;font-weight:700;font-size:16px;color:var(--gold);letter-spacing:.5px}
.nav{position:absolute;left:412px;top:40px;display:flex;gap:30px;font-size:12px;color:var(--ink);font-weight:500}
.nav .active{color:var(--gold);text-decoration:underline}
/* hero */
.hero{top:138px;left:0;width:1200px;height:506px;background:linear-gradient(120deg,#4b4536 0%,#6b5f3f 40%,#7a6a3f 65%,#4a4130 100%)}
.hero-title{top:268px;font-family:'Montserrat',sans-serif;font-weight:900;font-size:78px;letter-spacing:9px;color:#fff}
.hero-text{top:376px;font-size:12px;line-height:22px;color:#eee}
.arrow{position:absolute;top:373px;width:37px;height:37px;display:flex;align-items:center;justify-content:center;border-radius:2px}
/* welcome */
.welcome-title{top:748px}
.welcome-text{top:797px;font-size:11.5px;line-height:22.5px;left:235px;width:730px}
.script{top:896px;font-family:'Great Vibes',cursive;font-size:19px;color:var(--gold)}
.card{position:absolute;top:995px;width:203px;height:259px;border:1px solid var(--line);background:#fff;text-align:center}
.card.featured{border:2px solid var(--gold)}
.card .dot{position:absolute;left:71px;top:-30px;width:60px;height:60px;border-radius:50%;display:flex;align-items:center;justify-content:center}
.card h3{margin-top:78px;font-size:14px;font-weight:600;color:var(--ink)}
.card .rule{left:82px;top:115px}
.card p{margin-top:36px;font-size:10.5px;line-height:22.5px;padding:0 24px}
/* about */
.about{top:1314px;left:0;width:1200px;height:608px;background:var(--grey-bg)}
.about-text{position:absolute;left:158px;width:430px;font-size:10.5px;line-height:22.5px}
.badge{position:absolute;top:1570px;height:68px;background:#dfe6ea;border-radius:4px}
.photo{position:absolute;left:610px;top:1394px;width:427px;height:468px;background:linear-gradient(170deg,#bcd3e8 0%,#d9e4ea 30%,#c7cfc9 60%,#a8a79a 100%)}
.play{position:absolute;left:782px;top:1592px;width:84px;height:84px;border-radius:50%;background:#fff;border:6px solid rgba(201,150,42,.55);display:flex;align-items:center;justify-content:center}
/* services */
.svc-icon{position:absolute;top:2163px;width:74px;height:74px;border-radius:50%;border:2px solid var(--gold);display:flex;align-items:center;justify-content:center;background:#fff}
.svc-icon.solid{background:linear-gradient(135deg,var(--gold),var(--gold-light));border:none}
.svc{position:absolute;width:280px;text-align:center}
.svc h3{font-size:12px;font-weight:700;color:var(--ink);margin-top:2265px;}
.svc p{font-size:10.5px;line-height:22.5px}
/* purposes */
.panel{position:absolute;top:2541px;width:400px;height:306px;text-align:center;color:#fff}
.panel h2{margin-top:70px;font-family:'Montserrat',sans-serif;font-weight:700;font-size:24px;letter-spacing:1.5px;line-height:30px}
.panel p{margin-top:26px;font-style:italic;font-size:14px;font-weight:500}
.panel .btn{top:226px;left:138px;width:126px;height:35px}
/* quote */
.field{position:absolute;border:1px solid var(--gold-light);background:#fff;font-style:italic;font-size:10.5px;color:#b9b9b9;padding:14px 15px}
.worker{position:absolute;left:1010px;top:3030px;width:190px;height:359px;background:linear-gradient(180deg,#f1c83a 0%,#e9d9b7 22%,#c9d36a 55%,#b4c95a 100%);border-radius:90px 90px 0 0}
.scrap{position:absolute;left:0;top:3270px;width:390px;height:119px;background:radial-gradient(ellipse at 50% 100%,rgba(120,110,95,.18),rgba(255,255,255,0) 70%)}
/* footer */
.footer{top:3389px;left:0;width:1200px;height:90px;background:var(--gold)}
.footer nav{position:absolute;top:38px;left:0;width:1200px;display:flex;justify-content:center;font-family:'Montserrat',sans-serif;font-weight:700;font-size:10px;color:#fff}
.footer nav a{padding:0 15px;border-left:1px solid rgba(255,255,255,.8);line-height:14px}
.footer nav a:first-child{border-left:none}
.copy{top:3479px;left:0;width:1200px;height:38px;background:var(--dark);color:#ddd;font-size:9px;text-align:center;line-height:38px}
.copy em{color:var(--gold-light);font-style:normal}
</style>
</head>
<body>

<div class="abs topbar">
  <span style="left:160px"><svg width="10" height="13" viewBox="0 0 10 13"><path d="M5 0a5 5 0 0 0-5 5c0 4 5 8 5 8s5-4 5-8a5 5 0 0 0-5-5zm0 7a2 2 0 1 1 0-4 2 2 0 0 1 0 4z" fill="#e2b84c"/></svg>18 Harbourline Road, Singapore 700112</span>
  <span style="left:756px"><svg width="14" height="10" viewBox="0 0 14 10"><rect width="14" height="10" fill="#e2b84c"/><path d="M0 0l7 5 7-5" stroke="#2b2b2b" fill="none"/></svg>sales@tavorinmetal.com</span>
  <span style="left:936px"><svg width="12" height="12" viewBox="0 0 12 12"><path d="M2 0l2 3-1 2c1 2 2 3 4 4l2-1 3 2-1 2C5 12 0 7 0 2z" fill="#e2b84c"/></svg>+65-90001234</span>
</div>

<header class="abs header">
  <div class="brand"><i></i><b>TAVORIN METAL</b></div>
  <nav class="nav"><span class="active">HOME</span><span>ABOUT</span><span>OUR SERVICES</span><span>PRODUCTS</span><span>CONTACT US</span></nav>
  <div class="btn" style="left:905px;top:34px;width:134px;height:29px">Request a Quote</div>
</header>

<section class="abs hero" role="img" aria-label="Recycling machinery photograph with diamond photo tiles"></section>
<h1 class="abs center hero-title">Recycling</h1>
<p class="abs center hero-text">Lorem ipsum dolor amet af food truck vegan cray cold-pressed blog kale chips selvage migas.<br>Viral lomo pop-up, ethical sartorial blue bottle DIY skateboard jean shorts godard chia fixie</p>
<div class="arrow" style="left:158px;background:#fff"><svg width="10" height="14"><path d="M8 1L2 7l6 6" stroke="#c9962a" stroke-width="2" fill="none"/></svg></div>
<div class="arrow" style="left:1000px;background:var(--gold)"><svg width="10" height="14"><path d="M2 1l6 6-6 6" stroke="#fff" stroke-width="2" fill="none"/></svg></div>
<div class="btn" style="left:530px;top:460px;width:124px;height:37px">Discover More</div>

<svg class="abs" style="left:582px;top:702px" width="36" height="34" viewBox="0 0 36 34"><g fill="#e2c07a"><path d="M18 2l7 11h-6l-4-6zM6 31l-4-7 6-10 5 3-3 6h7v8zM30 31H20v-7l4 4 3-5h-4l4-5 5 6z"/></g></svg>
<h2 class="abs center heading welcome-title">Welcome To Tavorin Metal</h2>
<p class="abs welcome-text" style="text-align:center">Lorem ipsum dolor amet cardigan venmo biodiesel. XOXO normcore narwhal banjo distillery. Raclette VHS blog, cold-pressed four dollar toast yr green juice and stealopem activated charcoal banjo. Paleo typewriter cray PBR&amp;B cardigan, helvetica waistcoat hash-tag lyft vinyl neutra. Gastropub 3 wolf moon la croix. lyft selvage air plant pour-over</p>
<p class="abs center script">Lorem Ipsum Dolor</p>

<div class="card" style="left:160px"><div class="dot" style="background:#c9962a"><svg width="22" height="20" viewBox="0 0 22 20"><path d="M0 9L22 0 17 20 11 13 19 4 8 12z" fill="#fff"/></svg></div><h3>Lorem Ipsum</h3><div class="rule"></div><p>Lorem ipsum dolor amet cardigan venmo biodiesel. XOXO normcore narwhal banjo</p></div>
<div class="card featured" style="left:385px"><div class="dot" style="background:#e8a91c;left:70px;top:-31px"><svg width="22" height="20" viewBox="0 0 22 20"><path d="M0 9L22 0 17 20 11 13 19 4 8 12z" fill="#fff"/></svg></div><h3 style="margin-top:77px">Dolor Amet</h3><div class="rule" style="left:81px;top:114px"></div><p>Lorem ipsum dolor amet cardigan venmo biodiesel. XOXO normcore narwhal banjo</p></div>
<div class="card" style="left:610px"><div class="dot" style="background:#f3bf45"><svg width="22" height="20" viewBox="0 0 22 20"><path d="M0 9L22 0 17 20 11 13 19 4 8 12z" fill="#fff"/></svg></div><h3>Simply Dummy</h3><div class="rule"></div><p>Lorem ipsum dolor amet cardigan venmo biodiesel. XOXO normcore narwhal banjo</p></div>
<div class="card" style="left:834px"><div class="dot" style="background:#e3c068"><svg width="22" height="20" viewBox="0 0 22 20"><path d="M0 9L22 0 17 20 11 13 19 4 8 12z" fill="#fff"/></svg></div><h3>Valar Doprot</h3><div class="rule"></div><p>Lorem ipsum dolor amet cardigan venmo biodiesel. XOXO normcore narwhal banjo</p></div>

<section class="abs about"></section>
<p class="abs eyebrow" style="left:158px;top:1374px">About Us</p>
<h2 class="abs heading" style="left:158px;top:1389px">Who We Are</h2>
<div class="rule" style="left:158px;top:1437px"></div>
<p class="about-text" style="top:1455px">Tavorin Metal Recycling primary activities are the procurement, processing, recycling and trading of all ferrous and non-ferrous scrap metals, industrial scraps and other recyclables. We provide full-service ferrous and non-ferrous metal recycler and processor. Recognized as an industry leader in any metal recycling, our team of experienced staff</p>
<div class="badge" style="left:198px;width:58px;border-radius:50%;height:58px;top:1578px"></div>
<div class="badge" style="left:265px;width:72px;top:1578px;height:62px;background:#e6eef2;border:1px solid #bcd9e6"></div>
<div class="badge" style="left:345px;width:50px;top:1578px;height:62px;background:#7b86a8"></div>
<div class="badge" style="left:440px;width:110px;top:1572px;background:#f3ead6"></div>
<p class="about-text" style="top:1674px">We build long term relationships with all our customer by understanding their needs and recommending customized solutions that are designed to improve efficiency and value of their scrap.In the ever changing market environment, we constantly improve every aspect of our company, delivering consistent and reliable service and products to our clientele. Call us today to see how we can serve you</p>
<div class="btn" style="left:158px;top:1826px;width:126px;height:36px">More About Us</div>
<div class="photo" role="img" aria-label="Photograph of the company factory building with blue roof under a clear sky"></div>
<div class="play"><svg width="20" height="22"><path d="M2 1l17 10L2 21z" fill="#c9962a"/></svg></div>

<p class="abs center eyebrow" style="top:1981px">What We Do</p>
<h2 class="abs center heading" style="top:1996px">Our Services</h2>
<p class="abs" style="left:240px;width:720px;top:2061px;text-align:center;font-size:10.5px;line-height:22.5px">Lorem ipsum dolor amet subway tile post-ironic live-edge blue bottle 8-bit leggings plaid mustache forage shabby chic enamel pin fashion axe tote bag 3 wolf moon. Brooklyn butcher YOLO brunch beard. Photo booth tattooed fingerstache austin. humblebrag activated charcoal af tbh williamsburg.</p>

<div class="svc-icon" style="left:262px"><svg width="40" height="22" viewBox="0 0 40 22"><path d="M4 18a16 14 0 0 1 32 0z" fill="none" stroke="#c9962a" stroke-width="2"/><path d="M2 19h36M12 18l3-8M20 18V6M28 18l-3-8" stroke="#c9962a" stroke-width="2"/></svg></div>
<div class="svc-icon solid" style="left:561px"><svg width="36" height="36" viewBox="0 0 36 36"><circle cx="18" cy="18" r="11" fill="none" stroke="#fff" stroke-width="3" stroke-dasharray="5 3"/><circle cx="18" cy="18" r="5" fill="none" stroke="#fff" stroke-width="2"/></svg></div>
<div class="svc-icon" style="left:861px"><svg width="38" height="36" viewBox="0 0 38 36"><rect x="4" y="14" width="20" height="16" fill="none" stroke="#c9962a" stroke-width="2"/><circle cx="29" cy="11" r="6" fill="none" stroke="#c9962a" stroke-width="2"/><path d="M2 32h34M29 17v15" stroke="#c9962a" stroke-width="2"/></svg></div>

<div class="svc" style="left:159px;top:0"><h3>Prompt On-site/Off-site Quotation</h3><div class="rule" style="left:121px;top:2303px"></div><p style="margin-top:38px">Lorem ipsum dolor amet subway tile post-ironics live-edge blue bottle 8-bit leggings plaid mustache b forage shabby chic enamel pin fashion axe tote bag 3a</p></div>
<div class="svc" style="left:458px;top:0"><h3>Hassle Free Disposal Of Scrap Material</h3><div class="rule" style="left:121px;top:2303px"></div><p style="margin-top:38px">Lorem ipsum dolor amet subway tile post-ironics live-edge blue bottle 8-bit leggings plaid mustache b forage shabby chic enamel pin fashion axe tote bag 3a</p></div>
<div class="svc" style="left:758px;top:0"><h3>On Site Weighing Service</h3><div class="rule" style="left:121px;top:2303px"></div><p style="margin-top:38px">Lorem ipsum dolor amet subway tile post-ironics live-edge blue bottle 8-bit leggings plaid mustache b forage shabby chic enamel pin fashion axe tote bag 3a</p></div>
<div class="btn" style="left:536px;top:2445px;width:126px;height:35px">View All Services</div>

<div class="panel" style="left:0;background:linear-gradient(135deg,#3a3531,#5a4a3c 50%,#2f2b28)" role="img" aria-label="Photograph of scrap copper wires"><h2>FOR INDIVIDUAL<br>PURPOSES</h2><p>Do Your Part, Recycle With Us Today</p><div class="btn">Learn More</div></div>
<div class="panel" style="left:400px;background:linear-gradient(135deg,#b89033,#d7b45a 50%,#a9842d)" role="img" aria-label="Photograph of stacked brass rods"><h2>FOR CORPORATE<br>PURPOSES</h2><p>Get The Best Value For Your Scrap</p><div class="btn">Learn More</div></div>
<div class="panel" style="left:800px;background:linear-gradient(135deg,#2d2b29,#4a4540 50%,#26231f)" role="img" aria-label="Photograph of coiled metal scrap"><h2>FOR INTERNATIONAL<br>PURPOSES</h2><p>Your Trusted Global Partner</p><div class="btn">Learn More</div></div>

<div class="scrap" role="img" aria-label="Faint pile of scrap metal"></div>
<p class="abs center eyebrow" style="top:2920px">Do Not Hesitate</p>
<h2 class="abs center heading" style="top:2935px">Request a Quote</h2>
<div class="rule" style="left:581px;top:2984px"></div>
<div class="field" style="left:160px;top:3032px;width:278px;height:43px">Full Name</div>
<div class="field" style="left:461px;top:3032px;width:279px;height:43px">Phone Number</div>
<div class="field" style="left:762px;top:3032px;width:127px;height:43px">Date</div>
<div class="field" style="left:910px;top:3032px;width:127px;height:43px">Time</div>
<div class="field" style="left:160px;top:3099px;width:880px;height:111px">Your Message</div>
<div class="btn" style="left:538px;top:3257px;width:125px;height:35px">Submit Message</div>
<div class="worker" role="img" aria-label="Photograph of a smiling worker in a yellow hard hat and high-visibility vest"></div>

<footer class="abs footer"><nav><a>HOME</a><a>ABOUT</a><a>TERMS OF USE</a><a>PRIVACY</a><a>SITEMAP</a></nav></footer>
<div class="abs copy">© Copyright - <em>Tavorin Metal Recycling</em>. All Rights Reserved</div>

</body>
</html>
```